VineGlow Artbook for Okanagan Region, British Columbia

Creating an art book: VineGlow, for the Okanagan Wine Region in British Columbia, Canada. Would like smart, modern, clean and linear...cool, sexy urban, not ugly boring suburban... I need a cover that appeals to the wino in all of us! Title: VineGlow -Marla Pettivan
Updates
Thank you all kindly for your efforts. I have added some files so that you can get a sense of my aesthetic...it's never easy trying to figure it out, is it? I will hopefully have dimensions of book soon...cheers, Marla
would anyone please design a giant wine bottle with the wine label that looks like a label but says vineglow...just curious to see if it works as a design or not...thank you.
Target Market(s)
Designing this wine art book of quotes to wineries in Okanagan BC. Buyer is wine lover and tourist ready to spend his vacation bucks on this wonderful book!
Look and feel

```html
<!DOCTYPE html>
<html lang="en">
<head>
<meta charset="utf-8">
<title>VineGlow – Cover Variations</title>
<link rel="stylesheet" href="https://fonts.googleapis.com/css2?family=Jost:wght@500&family=Roboto:wght@300&display=swap">
<style>
  :root {
    --backdrop: #f4f4f4;
    --paper: #ffffff;
    --edge: #6e6e6e;
    --ink: #111111;
    --wine: #c4121f;
  }
  * { margin: 0; padding: 0; box-sizing: border-box; }
  html, body {
    width: 1200px;
    height: 806px;
    overflow: hidden;
    background: var(--backdrop);
  }
  .cover {
    position: absolute;
    top: 53px;
    width: 489px;
    height: 693px;
    background: var(--paper);
    border: 1px solid var(--edge);
  }
  .cover--medium { left: 94px; font-family: "Jost", sans-serif; font-weight: 500; }
  .cover--light { left: 639px; font-family: "Roboto", sans-serif; font-weight: 300; }

  .cover__author {
    position: absolute;
    top: 37px;
    right: 46px;
    font-size: 21px;
    line-height: 1;
    color: var(--ink);
    white-space: nowrap;
  }

  .cover__title {
    position: absolute;
    right: 44px;
    bottom: 37px;
    writing-mode: vertical-rl;
    transform: rotate(180deg);
    font-size: 74px;
    font-weight: inherit;
    font-style: normal;
    line-height: 1;
    color: var(--wine);
    white-space: nowrap;
  }
</style>
</head>
<body>
  <section class="cover cover--medium" aria-label="Cover variation in medium type">
    <p class="cover__author">Marla Pettivan</p>
    <h1 class="cover__title">VineGlow</h1>
  </section>

  <section class="cover cover--light" aria-label="Cover variation in light type">
    <p class="cover__author">Marla Pettivan</p>
    <h1 class="cover__title">VineGlow</h1>
  </section>
</body>
</html>
```